Lip Balm tube design

create label/ product print design for Lip balm tubes
Size of tube
76 mm high
24 mm wide

2.75 x 2" h- this is for the main part of tube, not top cap

Current design has been attached for reference. Would like to stick to something similar but need it to "pop" more and be more readable to user
Designs
Vanilla Mint
Citrus Spice
Coconut Lime
Marshmallow Creme
Satsuma Sugar

Designs must include product information (ingredients) as detailed on examples.
Color palette is color but soft, matte tones

```html
<!DOCTYPE html>
<html lang="en">
<head>
<meta charset="utf-8">
<title>Natural Lip Balm Labels</title>
<link rel="stylesheet" href="https://fonts.googleapis.com/css2?family=Libre+Baskerville:wght@700&family=Montserrat:wght@400;500&display=swap">
<style>
  :root {
    --stage: #3c414d;
    --coconut-bg-a: #dcdbd0;
    --coconut-bg-b: #f3f2e9;
    --coconut-ink: #5a4330;
    --coconut-accent: #8cb874;
    --citrus-bg-a: #f4b978;
    --citrus-bg-b: #fed3a0;
    --citrus-ink: #f26a1b;
    --panel: #ffffff;
    --leaf: #9cc48c;
  }
  * { margin: 0; padding: 0; box-sizing: border-box; }
  html, body { width: 1200px; height: 913px; overflow: hidden; background: var(--stage); }
  .stage { position: relative; width: 1200px; height: 913px; }
  .label {
    position: absolute; top: 76px; width: 413px; height: 760px; overflow: hidden;
    font-family: "Montserrat", sans-serif;
  }
  .label--coconut { left: 147px; color: var(--coconut-ink);
    background: linear-gradient(90deg, var(--coconut-bg-a) 0%, var(--coconut-bg-b) 25%, var(--coconut-bg-b) 75%, var(--coconut-bg-a) 100%); }
  .label--citrus { left: 640px; color: var(--citrus-ink);
    background: linear-gradient(90deg, var(--citrus-bg-a) 0%, var(--citrus-bg-b) 60%, var(--citrus-bg-a) 100%); }
  .label__frame { position: absolute; inset: 0; }
  .title { font-family: "Libre Baskerville", serif; font-weight: 700; }
  .info-panel {
    position: absolute; left: 112px; top: 0; width: 273px; height: 326px;
    background: linear-gradient(90deg, var(--panel) 60%, #ecebef 100%);
    border-radius: 0 0 30px 30px;
  }
  .info-panel__name {
    margin-top: 14px; text-align: center; font-size: 25px; font-weight: 400;
    letter-spacing: 4px; line-height: 30px;
  }
  .info-panel__art {
    position: absolute; left: 90px; top: 82px; width: 172px; height: 200px;
    background: radial-gradient(ellipse at center, #cfe3c4 0%, #e8f2e2 55%, rgba(255,255,255,0) 75%);
  }
  .info-panel__tagline {
    position: absolute; left: 16px; top: 264px; font-size: 16px; line-height: 24px;
  }
  .label--coconut .info-panel__tagline { color: var(--coconut-ink); }
  .product-art { position: absolute; }
  .product-art--coconut {
    left: 190px; top: 483px; width: 197px; height: 126px; border-radius: 50% 50% 45% 45%;
    background: radial-gradient(ellipse at 40% 45%, #d8cfc0 0%, #8a7561 45%, #5e4a38 80%, rgba(94,74,56,0) 100%);
  }
  .product-art--citrus {
    left: 151px; top: 417px; width: 234px; height: 211px; border-radius: 48%;
    background: radial-gradient(ellipse at 55% 50%, #f9a766 0%, #f4802e 45%, #f26a1b 70%, rgba(242,106,27,0) 100%);
  }
  .footer-origin {
    position: absolute; left: 55px; top: 704px; width: 140px; text-align: center;
    font-size: 15px; line-height: 17px;
  }
  .footer-weight {
    position: absolute; right: 21px; top: 719px; font-size: 15px; line-height: 17px;
  }
  .label--coconut .footer-origin, .label--coconut .footer-weight { color: var(--coconut-accent); }
</style>
</head>
<body>
<main class="stage">

  <section class="label label--coconut">
    <svg class="label__frame" width="413" height="760" viewBox="0 0 413 760">
      <g stroke="var(--coconut-ink)" stroke-width="2.5" fill="none">
        <path d="M50 0 V176 H60"/>
        <path d="M60 628 H50 V760"/>
      </g>
      <text class="title" transform="translate(76 609) rotate(-90)" font-size="70" fill="var(--coconut-ink)" textLength="412" lengthAdjust="spacingAndGlyphs">COCONUT</text>
      <text class="title" transform="translate(148 609) rotate(-90)" font-size="70" fill="var(--coconut-accent)" textLength="196" lengthAdjust="spacingAndGlyphs">LIME</text>
    </svg>
    <div class="info-panel">
      <h2 class="info-panel__name">NATURAL LIP<br>BALM</h2>
      <div class="info-panel__art" role="img" aria-label="Botanical sketch of a leafy green sprig"></div>
      <p class="info-panel__tagline">verda soy<br>plant | based | aromatherapy</p>
    </div>
    <div class="product-art product-art--coconut" role="img" aria-label="Engraved illustration of a whole and a halved coconut"></div>
    <p class="footer-origin">Made in Canada<br>100% Natural</p>
    <p class="footer-weight">Net WT. 302/8.5 G</p>
  </section>

  <section class="label label--citrus">
    <svg class="label__frame" width="413" height="760" viewBox="0 0 413 760">
      <g stroke="var(--citrus-ink)" stroke-width="2.5" fill="none">
        <path d="M50 0 V84 H60"/>
        <path d="M60 672 H50 V760"/>
      </g>
      <text class="title" transform="translate(77 656) rotate(-90)" font-size="70" fill="var(--citrus-ink)" textLength="558" lengthAdjust="spacingAndGlyphs">CITRUS SPICE</text>
    </svg>
    <div class="info-panel">
      <h2 class="info-panel__name">NATURAL LIP<br>BALM</h2>
      <div class="info-panel__art" role="img" aria-label="Botanical sketch of a leafy green sprig"></div>
      <p class="info-panel__tagline">verda soy<br>plant | based | aromatherapy</p>
    </div>
    <div class="product-art product-art--citrus" role="img" aria-label="Engraved illustration of a whole orange, a halved orange and leaves"></div>
    <p class="footer-origin">Made in Canada<br>100% Natural</p>
    <p class="footer-weight">Net WT. 302/8.5 G</p>
  </section>

</main>
</body>
</html>
```